Dentistry Office

We want a new design for a Dentist's office website.

The theme is: "We provide high quality, state-of-the-art, dental care in a comfortable, caring environment."

The site currently has a menu on the left of the page with about 40 items on it. There is a great deal of textual content on each page, plus several illustrations.

We want to do this using CSS, so we need specifications in the CSS for all possible elements. The CSS needs to be named in a logical manner for easy use.

Every dentist on the planet seems to use lots of Flash. We don't want to because it is so distracting. We are looking for an elegant solution targeting 24-55 age group, but not excluding anyone.

The following (from another dentist's site) can give you a taste of what we want to communicate on the site:

"After 20 years of teaching dentists how to refine their technique and many years of writing textbooks, I currently devote my time to my office and the hands-on practice of dentistry. I'd like to welcome you personally to my dental practice, and I invite you to meet my highly experienced team of professionals.

"We have offered complete dental care of the highest quality since 1978. We provide Preventive Services, Tooth Whitening and Cosmetic Dentistry for a beautiful smile, Endodontics (root canal treatment) to treat painful teeth, Sedation Dentistry so you can relax, and Dental Implants to restore what is missing. We offer total care.

"Our approach to your health is simple: We use our education, experience and dedication to provide every patient with superior dental care.

"This passion for excellence is not just a goal, but a standard every member of our team holds.

"We also pride ourselves with our state of the art procedures, training and technology. This includes creating a beautiful smile using techniques that preserve as much of the original tooth as possible.

"Our abilities are renowned throughout the dental profession and I hope if you have any questions you will contact us by an e-mail note, by phone or just by dropping by."

Keep in mind the screen shape and dimensions. Your design needs to work in the normal screen proportions, regardless of how it looks when you post it here. Scrolling is OK, but the first impression needs to work.

Keep in mind that there will be about 250 words, or more, on each page.

Competitors web sites:

http://www.brevalkoortho.example/

http://www.quimbelfieldcare.example/

http://www.grinsatdoverellclinic.example/

http://www.trunwickfamilydentalcare.example/

http://www.morvanhaledental.example/

http://www.ubrigandental.example/

We need to compete with these.

Target Market(s)

Generally adults seeking the most experienced and comfortable-to-be-with dentist.

Industry/Entity Type

Training

Requirements
Must have
• Must stand apart from other dentists.
• Must be elegant.
• Must have a horizontal menu structure across all columns, NOT a vertical that requires scrolling, no popout, pop down, etc. menus.
• We are looking for something special.
• Do not waste your time or ours putting up templates and things you have used before.
• Personally, I do not see how someone outside the US can understand the northern California dental market. But you are welcome to try.
Should not have
• Flash or graphics that move
• The look of a template
• Folksy fonts
• Looks like you used it 20 times before

```html
<!DOCTYPE html>
<html lang="en">
<head>
<meta charset="utf-8">
<title>Larkmoor Dentist — Harold Vennick, DDS, FAGD</title>
<link href="https://fonts.googleapis.com/css2?family=Noto+Sans:ital,wght@0,400;0,700;1,400;1,700&family=Arimo:wght@400;700&display=swap" rel="stylesheet">
<style>
:root{
  --slate:#6e7f87;
  --heading:#6f8189;
  --text:#8c979c;
  --link:#5e7079;
  --muted:#c3cacd;
  --rule:#d4d9db;
  --menu-rule:#a9b5ba;
  --panel:#e7eae7;
  --white:#ffffff;
}
*{margin:0;padding:0;box-sizing:border-box}
html,body{width:1200px;height:1022px;overflow:hidden;background:var(--white)}
body{position:relative;font-family:"Noto Sans",sans-serif;color:var(--text)}
a{color:var(--link)}

.site-brand{position:absolute;left:192px;top:28px}
.site-brand .name{font-size:27px;color:var(--heading);line-height:30px;font-weight:400}
.site-brand .doctor{font-size:17px;color:var(--muted);line-height:19px}

.top-nav{position:absolute;right:192px;top:55px;display:flex;font-size:10.8px}
.top-nav a{text-decoration:none;color:var(--muted);padding:3px 10px 6px;border-left:1px solid var(--rule)}
.top-nav a:first-child{border-left:none;color:var(--heading)}
.top-nav a:last-child{padding-right:0}

.topic-band{position:absolute;left:178px;top:98px;width:844px;height:244px;background:var(--slate);
  display:flex;padding:9px 0 0 14px;gap:20px}
.topic{width:147px}
.topic h2{font-family:"Arimo",sans-serif;font-weight:700;color:var(--white);font-size:17px;line-height:21px;height:51px}
.topic ul{list-style:none}
.topic li{font-family:"Arimo",sans-serif;font-size:10.2px;color:var(--white);height:18.75px;line-height:17.5px;
  white-space:nowrap;border-bottom:1px solid var(--menu-rule);padding-left:18px;position:relative}
.topic li::before{content:"";position:absolute;left:4px;top:6px;border-left:4px solid var(--white);border-top:3px solid transparent;border-bottom:3px solid transparent}
.topic li.last{border-bottom:none}
.topic li.info{border-bottom:none}
.topic li.info::before{display:none}

.main{position:absolute;left:192px;top:362px;width:502px}
.main h1,.main h2,.aside h2{font-weight:400;color:var(--heading);font-size:18px;line-height:26px;margin-bottom:12px}
.main p{font-size:10.6px;line-height:16.9px;margin-bottom:17px}
.main p.tight{margin-bottom:0}
.main strong{color:var(--link)}
.main hr{border:none;border-top:1px solid var(--rule);margin:18px 0 18px}
.signature{font-style:italic}

.aside{position:absolute;left:712px;top:362px;width:300px}
.services{list-style:none;font-size:10.6px;line-height:16.9px}
.services li{position:relative;padding-left:11px;margin-bottom:3.8px}
.services li::before{content:"";position:absolute;left:1px;top:6px;border-left:4px solid var(--text);border-top:3px solid transparent;border-bottom:3px solid transparent}
.services li.gap{margin-bottom:11px}

.contact-box{position:absolute;left:712px;top:747px;width:296px;height:115px;background:var(--panel);
  border:4px solid var(--slate);border-radius:3px;padding:6px 8px}
.contact-box h2{font-weight:400;color:var(--heading);font-size:18px;line-height:24px;margin-bottom:5px}
.contact-box p{color:var(--muted);font-size:12.2px;line-height:18.7px}
.contact-box .phone{color:var(--link);font-style:italic;font-weight:700}

.footer-rule{position:absolute;left:192px;top:951px;width:816px;border-top:1px solid var(--rule)}
.footer-nav{position:absolute;left:0;top:967px;width:1200px;display:flex;justify-content:center;gap:20px;font-size:10.4px}
.footer-nav a{text-decoration:none;color:var(--text)}
.copyright{position:absolute;left:0;top:995px;width:1200px;text-align:center;font-family:"Arimo",sans-serif;font-size:10px;color:var(--text)}
</style>
</head>
<body>

<header class="site-brand">
  <div class="name">Larkmoor Dentist</div>
  <div class="doctor">Harold Vennick, DDS, FAGD</div>
</header>

<nav class="top-nav">
  <a href="#">home</a><a href="#">why we are different</a><a href="#">technologie we offer</a><a href="#">meet dr. Vennick</a><a href="#">our staff</a><a href="#">contact us</a>
</nav>

<nav class="topic-band">
  <section class="topic"><h2>EDUCATION</h2>
    <ul><li>Emergency Dental Care</li><li>Your Mouth</li><li>Your Tooth</li><li>Cracked Tooth?</li><li>Missing a Tooth?</li><li>Sensitive Teeth</li><li>Dry Mouth</li><li>Tooth Grinding</li><li>Sleep Dentistry</li><li class="last">Videos</li></ul></section>
  <section class="topic"><h2>PREVENTATIVE</h2>
    <ul><li>What is Preventive Care?</li><li>Taking Care of Your Teeth</li><li>Eating Right</li><li>Dental Check-Ups</li><li>Sealants</li><li>Periodontal Disease</li><li>Kicking the Habit</li><li>Night Guards</li><li>Dental X-Rays</li><li class="last">Antibiotics with Treatment</li></ul></section>
  <section class="topic"><h2>COSMETICS</h2>
    <ul><li>Cosmetic Dentistry</li><li>Bleaching and Whitening</li><li>Cosmetic Bonding</li><li>Esthetic Veneers</li><li class="last">Tooth Shaping</li></ul></section>
  <section class="topic"><h2>RESTORATIONS</h2>
    <ul><li>Crowns/Caps: Each Step</li><li>CMBRs</li><li>Porcelain Bridges</li><li>Bonded Dental Bridges</li><li>Gold Restorations</li><li>Implants</li><li>Treating Cracked Teeth</li><li class="last">Periodontal (gum) Treatment</li></ul></section>
  <section class="topic"><h2>VISITING OUR OFFICE</h2>
    <ul><li>Where to Stay</li><li>First Visit / Map</li><li>Financial Policy</li><li class="last">Dental Insurance</li>
    <li class="info">Harold Vennick, DDS, FAGD</li><li class="info">2240 Larkmoor Ave. Ste B</li><li class="info">Larkmoor, CA 95999</li><li class="info">707-555-0142</li></ul></section>
</nav>

<main class="main">
  <h1>Welcome to our website</h1>
  <p>In Larkmoor, when you’re a patient of Dr. Vennick, you can be confident that you’re receiving care from the most experienced, knowledgeable, and skilled <a href="#">cosmetic dentist</a> in Larkmoor County.</p>
  <p>Dr. Vennick is an award-winning leader in restorative dentistry and a genial professional. His humor, dedication, and talent ensure you a pleasant experience and superb, long-lasting results.</p>
  <hr>
  <h2>Dr. Vennick’s Commitment</h2>
  <p>After 25 years of teaching dentists how to refine their technique and many years of writing textbooks, I currently devote my time to my office and the hands-on practice of dentistry. I'd like to welcome you personally to my dental practice, and I invite you to meet my highly experienced <a href="#">team of professionals</a>.</p>
  <p class="tight">Dr. Vennick and his Associated have offered complete dental care of the highest quality since 1978. We provide <a href="#">Preventive Services</a>, Tooth Whitening and <a href="#">Cosmetic Dentistry</a> for a beautiful smile, Endodontics (root canal treatment) to treat painful teeth, <a href="#">Sedation Dentistry</a> so you can relax, and <a href="#">Dental Implants</a> to restore what is missing. We offer total care. Our approach to your health is simple: <strong>We use our education, experience and dedication to provide every patient with <a href="#">superior dental care</a></strong>. This passion for excellence is not just a goal, but a standard every member of our team holds.</p>
  <p class="tight">We also pride ourselves with our state of the art procedures, training and technology. This includes creating a beautiful smile using techniques that preserve as much of the original tooth as possible.</p>
  <p>Our abilities are renowned throughout the dental profession and I hope if you have any questions you will contact us by an <a href="#">e-mail</a> note, by phone or just by dropping by.</p>
  <p>Thank you.<br>Sincerely,</p>
  <p class="signature">Harold Vennick, DDS FAGD</p>
</main>

<aside class="aside">
  <h2>Dr. Vennick Provides</h2>
  <ul class="services">
    <li>General dentistry—oral hygiene, cavity detection and repair, crowns.</li>
    <li>Cosmetic/restorative dentistry—broken or misshapen teeth, crooked smiles, unsightly gaps</li>
    <li>Non-metal fillings—nontoxic, durable tooth-colored resin fillings that are proven to provide better results</li>
    <li>Tooth shaping—extending, shortening or otherwise reshaping teeth for improved esthetics</li>
    <li>Complete smile make-over's—resin veneers that reshape the whole mouth while preserving natural teeth</li>
    <li>Tooth whitening—at-home bleaching options to make teeth appear years younger</li>
    <li>Laser Dentistry, Sleep Dentistry, and Implant Dentistry with the Finest and Latest Equipment and Materials.</li>
    <li class="gap">Dental Implants to replace missing teeth.</li>
    <li>Sedation Dentistry so you can be relaxed.</li>
  </ul>
</aside>

<section class="contact-box">
  <h2>Contact Us</h2>
  <p>Please contact us at <span class="phone">(707) 555-0142</span>.<br>To contact us outside office hours for an emergency, please call <span class="phone">(707) 555-0178</span>.</p>
</section>

<div class="footer-rule"></div>
<nav class="footer-nav">
  <a href="#">home</a><a href="#">why we are different</a><a href="#">technologie we offer</a><a href="#">meet dr. Vennick</a><a href="#">our staff</a><a href="#">contact us</a>
</nav>
<p class="copyright">Copyright © 2010 drvennick.example. All right reserved.</p>

</body>
</html>
```